One page flyer for nonprofit focused IT company

I need a one page flyer (one side of a single 8.5x11 page) with text and graphics. The company logo is already done, and it must appear on the flyer along with other icons and graphics. The final design will be printed on heavy weight glossy paper as a handout and also distributed as a PDF.

The text is provided in an attachment, if it needs to be shortened let me know.

Industry/Entity Type

Information Technology

Requirements
Must have
• some flare (colors, icons or images)
Should not have
• While we work for nonprofits, my company is a FOR PROFIT company.

```html
<!DOCTYPE html>
<html lang="en">
<head>
<meta charset="utf-8">
<title>Northfield Systems – 50 Years of Nonprofit IT Services</title>
<link href="https://fonts.googleapis.com/css2?family=Oswald:wght@600;700&family=Roboto+Condensed:wght@400;700&display=swap" rel="stylesheet">
<style>
  :root {
    --bg: #808080;
    --paper: #ffffff;
    --crimson: #98182c;
    --crimson-deep: #6e0f1e;
    --crimson-soft: #c98a95;
    --heading: #1e2f1a;
    --body: #4a4a4a;
    --rule: #e3e3e3;
    --photo-a: #cfd6e0;
    --photo-b: #8a97aa;
  }
  * { box-sizing: border-box; margin: 0; padding: 0; }
  html, body { width: 1200px; height: 1200px; overflow: hidden; background: var(--bg); }
  .flyer {
    position: absolute; left: 150px; top: 18px;
    width: 900px; height: 1164px;
    background: var(--paper);
    font-family: "Roboto Condensed", Arial, sans-serif;
    overflow: hidden;
  }
  .hero-band { position: absolute; left: 0; top: 0; width: 900px; height: 460px; }
  .hero-photo {
    position: absolute; left: 455px; top: 215px; width: 365px; height: 240px;
    background: linear-gradient(135deg, var(--photo-a), var(--photo-b) 60%, #dfe5ec);
  }
  .headline { position: absolute; left: 45px; top: 95px; color: #fff; font-family: "Oswald", Arial, sans-serif; }
  .headline .big { font-size: 104px; font-weight: 700; line-height: 1; letter-spacing: -1px; }
  .headline .sub { font-size: 46px; font-weight: 600; line-height: 1.05; margin-top: 8px; text-transform: uppercase; }
  .headline .underline { width: 130px; height: 4px; background: #fff; margin-top: 14px; }
  .brand {
    position: absolute; left: 545px; top: 118px; width: 255px;
    display: flex; align-items: center; gap: 10px;
    color: var(--crimson); font-weight: 700; font-size: 25px; letter-spacing: 1px; text-transform: uppercase;
  }
  .brand .mark { width: 34px; height: 34px; background: var(--crimson); flex: none; }
  .column { position: absolute; top: 465px; }
  .column.left { left: 45px; width: 375px; }
  .column.right { left: 475px; width: 395px; top: 480px; }
  .divider { position: absolute; left: 445px; top: 470px; width: 1px; height: 440px; background: var(--rule); }
  .item { margin-bottom: 30px; }
  .column.right .item { margin-bottom: 26px; }
  .item h2 {
    position: relative; padding-left: 30px;
    color: var(--heading); font-size: 17px; font-weight: 700; line-height: 1.05; text-transform: uppercase;
  }
  .item h2::before {
    content: ""; position: absolute; left: 0; top: 1px; width: 16px; height: 14px;
    background: linear-gradient(90deg, var(--crimson) 50%, var(--crimson-soft) 50%);
  }
  .item p { margin-top: 8px; color: var(--body); font-size: 11.5px; line-height: 1.3; }
  .bottom-photo {
    position: absolute; left: 420px; top: 880px; width: 480px; height: 205px;
    background: linear-gradient(to bottom, rgba(255,255,255,1), rgba(255,255,255,0) 35%),
                linear-gradient(to right, rgba(255,255,255,1), rgba(255,255,255,0) 30%),
                linear-gradient(135deg, #d9dee6, var(--photo-b) 55%, #c4ccd8);
  }
  .footer {
    position: absolute; left: 0; bottom: 0; width: 900px; height: 80px;
    background: var(--crimson); border-top: 5px solid #fff;
    display: flex; align-items: center; justify-content: center; gap: 14px;
    color: #fff; font-weight: 700; font-size: 24px; letter-spacing: 5px; text-transform: uppercase;
  }
</style>
</head>
<body>
<div class="flyer">
  <svg class="hero-band" viewBox="0 0 900 460" aria-hidden="true">
    <polygon points="0,22 482,22 535,212 455,420 0,420" fill="var(--crimson)"/>
    <polygon points="0,210 535,212 455,420 0,420" fill="var(--crimson)" opacity="0.9"/>
    <polygon points="470,22 482,22 535,212 505,212" fill="var(--crimson-deep)"/>
  </svg>
  <div class="hero-photo" role="img" aria-label="Photo of a presenter speaking to colleagues around a meeting table in a bright office"></div>

  <div class="headline">
    <div class="big">50 YEARS</div>
    <div class="sub">Of Nonprofit IT<br>Services</div>
    <div class="underline"></div>
  </div>

  <div class="brand"><span class="mark"></span><span>Northfield Systems</span></div>

  <div class="divider"></div>

  <section class="column left">
    <div class="item">
      <h2>An efficient and elegant approach to IT solution implementations</h2>
      <p>Northfield Systems Corporation has been supporting the Information Systems needs of nonprofits for over 50 years. We continually strive to bring the latest technologies and best practices to nonprofits to drive down the cost of IT while implementing systems that drive revenue. Our Agile approach to IT management means that we deliver working systems to every one of our clients every two week</p>
    </div>
    <div class="item">
      <h2>90% reduction in software development costs</h2>
      <p>Harbor Point's Regional Auto Dealers Guild needed to update their core product offering; they engaged their in-house IT department who estimated the project would take 3 years at a cost of $3,000,000. RADG decided to work with Northfield Systems Corporation instead, and the product was released to production in only 9 months at one tenth of the cost, only $300,000</p>
    </div>
    <div class="item">
      <h2>10X increase in membership</h2>
      <p>Greenway Paths Alliance needed to move to online membership registration and contracted with Northfield Systems Corporation to build a significant online presence and engage potential members. Through compelling online tools and mobile applications Greenway Paths has increased membership 10 fold.</p>
    </div>
    <div class="item">
      <h2>20% reduction in overhead</h2>
      <p>The National League for Women Leaders had antiquated systems and processes in place to manage over 500 chapters across the nation. Working with NSC they implemented online tools to allow communication and management between the local chapters and national headquarters. This eliminated much of the overhead of chapter management, reducing HR costs by 20%.</p>
    </div>
  </section>

  <section class="column right">
    <div class="item">
      <h2>Mobile applications</h2>
      <p>Northfield Systems Corporation implements mobile applications for phones and tablets to provide direct communications with members and donors enabling real-time, two way interaction</p>
    </div>
    <div class="item">
      <h2>Systems integration</h2>
      <p>Every nonprofit's IT applications are scattered and disconnected. Northfield Systems Corporation has decades of experience integrating these applications into a single cohesive system</p>
    </div>
    <div class="item">
      <h2>Business intelligence and reporting</h2>
      <p>Northfield Systems Corporation can wrestle all of an organization's data into simple executive dashboards and reports.</p>
    </div>
    <div class="item">
      <h2>Cloud migration</h2>
      <p>Reduce IT costs by migrating to the latest cloud solutions.</p>
    </div>
    <div class="item">
      <h2>Member donor database</h2>
      <p>Northfield Systems Corporation's GiveLedger Member / Donor CRM system is fully customized for each client meeting the unique needs of your organization.</p>
    </div>
  </section>

  <div class="bottom-photo" role="img" aria-label="Faded photo of business people shaking hands in an office"></div>

  <footer class="footer">
    <svg width="20" height="20" viewBox="0 0 20 20" aria-hidden="true">
      <g fill="none" stroke="#fff" stroke-width="1.6">
        <circle cx="10" cy="10" r="8.5"/>
        <ellipse cx="10" cy="10" rx="3.8" ry="8.5"/>
        <line x1="1.5" y1="10" x2="18.5" y2="10"/>
        <path d="M3 5.5h14M3 14.5h14"/>
      </g>
    </svg>
    <span>northfieldsystems.com</span>
  </footer>
</div>
</body>
</html>
```